Website Design - Financial Services Software

We are looking for website designs for our public website.
Some competitor sites we like are
www.ledgerwick.com.au
www.pluvo.com.au
www.plannerbeam.com
www.quorvia.com.au

A wireframe example of our site can be found at
http://tmw4rp.draftpane.com/

Attached is our logo.

Industry/Entity Type

Financial

```html
<!DOCTYPE html>
<html lang="en">
<head>
<meta charset="utf-8">
<title>Fidentra – Smarter Financial Strategies</title>
<link href="https://fonts.googleapis.com/css2?family=Noto+Serif:wght@400&family=Open+Sans:wght@300;400;600&display=swap" rel="stylesheet">
<style>
:root{
  --ink:#1e1e1e;
  --text:#3a3a3a;
  --muted:#b9b9b9;
  --accent:#0a7ba8;
  --band:#2b2b2b;
  --band-light:#3b3b3b;
  --slide-bg:#ededea;
  --footer:#3a3a3a;
  --footer-base:#262626;
  --footer-text:#e6e6e6;
  --tick:#5a9a1a;
  --quote:#19b4e8;
  --white:#ffffff;
}
*{margin:0;padding:0;box-sizing:border-box}
html,body{width:964px;height:1200px;overflow:hidden;background:var(--white)}
body{position:relative;font-family:"Open Sans",Arial,sans-serif;color:var(--text)}
.abs{position:absolute}
.serif{font-family:"Noto Serif",Georgia,serif}

/* header */
.brand{left:159px;top:60px;display:flex;align-items:center;gap:8px}
.brand-mark{width:14px;height:14px;background:var(--ink)}
.brand-name{font-family:"Noto Serif",Georgia,serif;font-size:24px;color:var(--ink);letter-spacing:1px}
.brand-tagline{left:159px;top:116px;font-family:"Noto Serif",Georgia,serif;font-size:7px;letter-spacing:1px;color:var(--ink);text-transform:uppercase}
.utility{right:227px;top:17px;font-size:11px;color:#555;display:flex;white-space:nowrap}
.utility span{padding:0 4px;border-left:1px solid #bbb;line-height:12px}
.utility span:first-child{border-left:none}
.utility span:last-child{padding-right:0}
.login{left:748px;top:16px;width:58px;height:19px;background:var(--accent);color:var(--white);font-size:11px;font-weight:600;text-align:center;line-height:19px}
.nav{display:flex;font-size:12px;color:var(--ink);white-space:nowrap}
.nav span{padding:0 11px;border-left:1px solid #999;line-height:14px}
.nav span:first-child{border-left:none}
.main-nav{right:146px;top:109px}
.main-nav span:last-child{padding-right:0}

/* hero */
.band{left:0;top:135px;width:964px;height:231px;background:linear-gradient(180deg,var(--band-light),var(--band))}
.slide{left:158px;top:150px;width:648px;height:236px;background:var(--slide-bg);box-shadow:0 2px 3px rgba(0,0,0,.25)}
.slide-photo{left:0;top:0;width:362px;height:236px;background:linear-gradient(100deg,#d8d3c7 0%,#b9ad98 40%,#5e5a55 75%,#e6e5e1 100%)}
.slide-title{left:362px;top:48px;width:286px;text-align:center;font-size:20px;color:var(--ink)}
.slide-sub{left:362px;top:85px;width:286px;text-align:center;font-size:14px;font-weight:300;line-height:16px;color:var(--ink)}
.ghost-btn{width:113px;height:33px;border:2px solid #555;font-size:13px;font-weight:300;color:var(--ink);text-align:center;line-height:29px}
.dots{left:477px;top:218px;display:flex;gap:6px}
.dots i{width:8px;height:8px;border-radius:50%;background:var(--ink)}
.dots i:first-child{background:var(--white);border:1px solid var(--ink)}

/* call to action */
.cta-text{left:265px;top:414px;font-size:12px;color:var(--text)}
.dark-btn{background:var(--ink);color:var(--white);text-align:center}
.cta-btn{left:577px;top:412px;width:102px;height:22px;font-size:12px;line-height:22px}

/* intro */
.intro-title{left:158px;top:465px;font-size:19px;color:var(--ink)}
.intro-copy{left:158px;top:494px;width:310px;font-size:9.6px;line-height:12.4px;color:var(--ink)}
.ticks{left:156px;top:564px;list-style:none;font-size:10.5px;color:var(--ink)}
.ticks li{display:flex;align-items:center;gap:6px;height:16.5px}
.learn-btn{left:156px;top:629px;width:102px;height:22px;font-size:12px;line-height:22px}
.video{left:489px;top:470px;width:317px;height:191px;background:linear-gradient(90deg,#4a3a2c,#8a7c66 45%,#5d4b38)}
.video-top{left:0;top:0;width:317px;height:18px;background:rgba(0,0,0,.6)}
.video-bar{left:0;top:165px;width:317px;height:26px;background:#1b1b1b}
.video-progress{left:0;top:162px;width:317px;height:4px;background:#c8151b}
.play{left:138px;top:82px;width:40px;height:28px;border-radius:7px;background:#111}

/* columns */
.col-title{font-size:13.5px;color:var(--ink)}
.col-sub{font-size:11px;font-weight:600;color:var(--muted)}
.frame{width:206px;height:132px;background:var(--white);border:1px solid #ddd;box-shadow:0 1px 3px rgba(0,0,0,.12);padding:5px}
.frame div{width:100%;height:100%}
.col-copy{width:206px;font-size:9.2px;line-height:12.6px;letter-spacing:.2px;color:var(--ink)}
.more{width:112px;height:22px;border:1px solid #ccc;border-radius:2px;background:linear-gradient(#fff,#eee);font-size:8px;color:var(--accent);line-height:20px;padding-left:9px}
.more svg{position:absolute;right:6px;top:8px}
.divider{left:160px;top:1001px;width:640px;height:1px;background:#e6e6e6}

/* footer */
.footer{left:0;top:1018px;width:964px;height:136px;background:var(--footer);border-top:6px solid #555}
.footer-base{left:0;top:1154px;width:964px;height:46px;background:var(--footer-base)}
.f-head{top:1034px;font-size:13.5px;color:var(--white)}
.f-links{top:1068px;font-size:10px;line-height:16.5px;color:var(--footer-text)}
.quote{left:158px;top:1070px;width:200px;font-size:10px;line-height:10.5px;color:var(--footer-text)}
.quote-name{left:317px;top:1116px;font-size:11px;font-style:italic;font-weight:600;color:var(--quote)}
.foot-nav{left:356px;top:1172px;color:var(--white)}
</style>
</head>
<body>

<header>
  <div class="abs brand"><span class="brand-mark"></span><span class="brand-name">FIDENTRA</span></div>
  <div class="abs brand-tagline">Smarter Financial Strategies</div>
  <div class="abs utility"><span>Support</span><span>Contact Us</span><span>Sign Up</span></div>
  <div class="abs login">Login</div>
  <nav class="abs nav main-nav"><span>HOME</span><span>FEATURES</span><span>FAQ</span><span>ABOUT US</span></nav>
</header>

<section class="abs band"></section>
<section class="abs slide">
  <div class="abs slide-photo" role="img" aria-label="Photo of smiling business team in suits"></div>
  <h1 class="abs slide-title serif" style="font-weight:400">Smarter Financial Strategies</h1>
  <p class="abs slide-sub">Values and Cash-flow focused financial<br>software for financial planners</p>
  <div class="abs ghost-btn" style="left:361px;top:142px">feature tour</div>
  <div class="abs ghost-btn" style="left:491px;top:142px">feature tour</div>
  <div class="abs dots"><i></i><i></i><i></i><i></i></div>
</section>

<p class="abs cta-text">Create an account today and begin your 30 day trial</p>
<div class="abs dark-btn cta-btn">Sign Up Now</div>

<h2 class="abs intro-title serif" style="font-weight:400">Smarter Financial Strategies</h2>
<p class="abs intro-copy">Lorem Ipsum is simply dummy text of the printing and typesetting industry. Lorem Ipsum has been the industry's standard dummy text ever since the 1500s. Lorem Ipsum is simply dummy text of the printing and typesetting industry. Lorem Ipsum has been the industry's standard dummy text ever since the 1500s.</p>
<ul class="abs ticks">
  <li><svg width="14" height="11" viewBox="0 0 14 11"><path d="M1 6l4 4 8-9" fill="none" stroke="var(--tick)" stroke-width="2.6"/></svg>Dummy text ever since the 1500s</li>
  <li><svg width="14" height="11" viewBox="0 0 14 11"><path d="M1 6l4 4 8-9" fill="none" stroke="var(--tick)" stroke-width="2.6"/></svg>Of the printing and typesetting</li>
  <li><svg width="14" height="11" viewBox="0 0 14 11"><path d="M1 6l4 4 8-9" fill="none" stroke="var(--tick)" stroke-width="2.6"/></svg>Dummy text ever since the 1500s</li>
</ul>
<div class="abs dark-btn learn-btn">Learn More</div>

<div class="abs video" role="img" aria-label="Video still of a presenter in an office with bookshelves">
  <div class="abs video-top"></div>
  <div class="abs play"><svg width="40" height="28" viewBox="0 0 40 28"><path d="M16 8l10 6-10 6z" fill="#fff"/></svg></div>
  <div class="abs video-progress"></div>
  <div class="abs video-bar">
    <svg class="abs" style="left:14px;top:7px" width="12" height="12" viewBox="0 0 12 12"><path d="M2 1l9 5-9 5z" fill="#999"/></svg>
    <svg class="abs" style="left:46px;top:7px" width="14" height="12" viewBox="0 0 14 12"><path d="M1 4h3l4-3v10L4 8H1z" fill="#999"/></svg>
    <span class="abs" style="left:74px;top:7px;font-size:8px;color:#fff">0:00</span>
    <span class="abs" style="left:253px;top:8px;width:22px;height:10px;background:#666"></span>
    <svg class="abs" style="left:295px;top:7px" width="12" height="12" viewBox="0 0 12 12"><path d="M1 4V1h3M8 1h3v3M11 8v3H8M4 11H1V8" fill="none" stroke="#bbb"/></svg>
  </div>
</div>

<h3 class="abs col-title serif" style="left:161px;top:696px;font-weight:400">Our Products</h3>
<p class="abs col-sub" style="left:160px;top:712px">What we do</p>
<div class="abs frame" style="left:156px;top:739px"><div role="img" aria-label="Photo of a laughing man" style="background:linear-gradient(90deg,#f2f2f2,#8a5a3e 50%,#f2f2f2)"></div></div>
<p class="abs col-copy" style="left:159px;top:879px">Sed ut perspiciatis unde omnis iste natus error sit voluptatem accusantium doloremque laudantium, totam rem aperiam, eaque ipsa quae ab illo inventore veritatis et quasi architecto beatae vitae dicta sunt</p>
<div class="abs more" style="left:158px;top:956px">Learn More<svg width="12" height="5" viewBox="0 0 12 5"><path d="M0 2.5h11M8 0l3 2.5L8 5" fill="none" stroke="#888"/></svg></div>

<h3 class="abs col-title serif" style="left:378px;top:696px;font-weight:400">Our Partners</h3>
<p class="abs col-sub" style="left:377px;top:712px">Our Clients</p>
<div class="abs frame" style="left:377px;top:739px"><div role="img" aria-label="Photo of a man reading a newspaper" style="background:linear-gradient(90deg,#f4f4f4 25%,#c9a58c 60%,#4a3a30)"></div></div>
<p class="abs col-copy" style="left:381px;top:879px">Nemo enim ipsam voluptatem quia voluptas sit aspernatur aut odit aut fugit, sed quia consequuntur magni dolores eos qui ratione voluptatem sequi nesciun tdolore magnam aliquam quaerat voluptatem.</p>
<div class="abs more" style="left:380px;top:956px">Learn More<svg width="12" height="5" viewBox="0 0 12 5"><path d="M0 2.5h11M8 0l3 2.5L8 5" fill="none" stroke="#888"/></svg></div>

<h3 class="abs col-title serif" style="left:598px;top:696px;font-weight:400">Our Blog</h3>
<p class="abs col-sub" style="left:597px;top:712px">Stay tuned for our news</p>
<div class="abs frame" style="left:597px;top:739px"><div role="img" aria-label="Photo of a smiling businesswoman holding glasses" style="background:linear-gradient(90deg,#b9c0c8,#e8cbb6 50%,#6a7078)"></div></div>
<p class="abs col-copy" style="left:602px;top:879px">Neque porro quisquam est, qui dolorem ipsum quia dolor sit amet, consectetur, adipisci velit, sed quia non numquam eius modi tempora incidunt ut labore et dolore magnam aliquam quaerat voluptatem.</p>
<div class="abs more" style="left:601px;top:956px">Learn More<svg width="12" height="5" viewBox="0 0 12 5"><path d="M0 2.5h11M8 0l3 2.5L8 5" fill="none" stroke="#888"/></svg></div>

<div class="abs divider"></div>

<footer>
  <div class="abs footer"></div>
  <div class="abs footer-base"></div>
  <h4 class="abs f-head serif" style="left:160px;font-weight:400">Testimonials</h4>
  <p class="abs quote">Lorem Ipsum is simply dummy text of the printing and typesetting industry. Lorem Ipsum has been the industry's standard dummy text ever since the 1500s.</p>
  <p class="abs quote-name">Helena R.</p>
  <h4 class="abs f-head serif" style="left:381px;font-weight:400">About</h4>
  <p class="abs f-links" style="left:379px">About Us<br>Support</p>
  <h4 class="abs f-head serif" style="left:490px;font-weight:400">Legal</h4>
  <p class="abs f-links" style="left:490px">Terms of USe<br>Privacy</p>
  <h4 class="abs f-head serif" style="left:579px;font-weight:400">Getting Started</h4>
  <p class="abs f-links" style="left:579px">Why Fidentra<br>Download a Summary<br>Fidentra Videos</p>
  <h4 class="abs f-head serif" style="left:709px;font-weight:400">Connect</h4>
  <p class="abs f-links" style="left:709px">Fidentra on Linkora<br>Fidentra on Chirpwire</p>
  <nav class="abs nav foot-nav"><span>HOME</span><span>FEATURES</span><span>FAQ</span><span>ABOUT US</span></nav>
</footer>

</body>
</html>
```